Progressive Architecture and Urban Planning Studio - Stationery Design

The Kestrel Collective: a small boutique Architectural and Urban Planning Studio based in Natal/ RN, Brazil, about to open branches in South Africa and West Africa, established to provide high quality, innovative design and personal client service for projects worldwide. Our approach to Architecture: Minimal - Less is More, so to speak, but with an edge! Strive to produce "clean" projects - stripped of all that can be stripped, no excesses. Got our Logo right here with Pixel Harbor, and hope to do the same with our stationery (were informed that includes business cards, letterhead and envelopes). Since we'll be using two clour schemes, we want at least one using a black background (business card). We'll also allow manipulation of our logo if it helps the final design. Good Luck!

Industry/Entity Type

Business

Other font styles liked:
• Nexa

Colors

Designer to choose colors to be used in the design.

Requirements
Must have
• Business Cards/ Letterheads with the following address:
Rua Benedito Sarmento 742, Morro Branco, Natal/RN
Should be able to edit it.

```html
<!DOCTYPE html>
<html lang="en">
<head>
<meta charset="utf-8">
<title>The Kestrel Collective – Envelope</title>
<link href="https://fonts.googleapis.com/css2?family=Montserrat:wght@400;600&family=Arimo:wght@400;700&display=swap" rel="stylesheet">
<style>
  :root {
    --backdrop: #d4d4d4;
    --paper: #ffffff;
    --fold-line: #8a8a8a;
    --ink: #1a1a1a;
    --accent: #d6141c;
    --faint: #f1f1f1;
  }
  html, body {
    margin: 0;
    padding: 0;
    width: 1200px;
    height: 1000px;
    overflow: hidden;
    background: var(--backdrop);
  }
  .canvas {
    position: relative;
    width: 1200px;
    height: 1000px;
  }
  .envelope-back {
    position: absolute;
    left: 59px;
    top: 21px;
    width: 1077px;
    height: 468px;
    background: var(--paper);
  }
  .envelope-back svg {
    position: absolute;
    inset: 0;
  }
  .flap-mark {
    position: absolute;
    left: 0;
    right: 0;
    top: 84px;
    text-align: center;
    font-family: "Montserrat", sans-serif;
    font-weight: 600;
    font-size: 17px;
    letter-spacing: 3px;
    text-transform: uppercase;
    color: var(--accent);
  }
  .envelope-front {
    position: absolute;
    left: 59px;
    top: 519px;
    width: 1077px;
    height: 468px;
    background: var(--paper);
    overflow: hidden;
  }
  .brand {
    position: absolute;
    left: 33px;
    top: 32px;
    display: flex;
    align-items: center;
    gap: 20px;
  }
  .brand-square {
    width: 40px;
    height: 40px;
    background: var(--accent);
  }
  .brand-name {
    font-family: "Montserrat", sans-serif;
    font-weight: 400;
    font-size: 24px;
    letter-spacing: 7px;
    text-transform: uppercase;
    color: var(--ink);
  }
  .faint-name {
    position: absolute;
    right: -40px;
    bottom: 10px;
    font-family: "Montserrat", sans-serif;
    font-weight: 600;
    font-size: 130px;
    line-height: 1;
    color: var(--faint);
    letter-spacing: 4px;
    text-transform: uppercase;
    white-space: nowrap;
  }
  .contact {
    position: absolute;
    left: 17px;
    top: 374px;
    font-family: "Arimo", sans-serif;
    font-size: 10.5px;
    line-height: 14px;
    color: var(--ink);
  }
  .contact p { margin: 0; }
  .contact .address { margin-bottom: 5px; }
  .contact .gap { margin-top: 5px; }
  .contact .label {
    color: var(--accent);
    font-weight: 700;
  }
</style>
</head>
<body>
<div class="canvas">
  <section class="envelope-back">
    <svg width="1077" height="468" viewBox="0 0 808 351" fill="none" stroke="var(--fold-line)" stroke-width="1">
      <rect x="0.5" y="0.5" width="807" height="350"/>
      <path d="M0 0 C10 30 20 50 34 54 L301 136 C360 152 430 152 486 138 L774 54 C790 48 798 30 808 0"/>
      <path d="M34 54 L34 304"/>
      <path d="M774 54 L774 304"/>
      <path d="M0 351 C15 330 22 312 34 304 C42 296 50 291 60 291 L748 291 C760 291 768 296 774 304 C786 312 795 330 808 351"/>
    </svg>
    <div class="flap-mark">The Kestrel Collective</div>
  </section>

  <section class="envelope-front">
    <div class="brand">
      <span class="brand-square"></span>
      <span class="brand-name">The Kestrel Collective</span>
    </div>
    <div class="faint-name" aria-hidden="true">Kestrel</div>
    <div class="contact">
      <p class="address">Rua Benedito Sarmento 742, Morro Branco, Natal/RN</p>
      <p><span class="label">Tel :</span> +000 000 0000</p>
      <p><span class="label">Mob :</span> +000 000 0000</p>
      <p class="gap"><span class="label">E-mail :</span> name@kestrelcollective.com</p>
      <p><span class="label">Web :</span> www.kestrelcollective.com</p>
    </div>
  </section>
</div>
</body>
</html>
```